Professional & attention grabbing.

A business card design, front and back. I already have a logo I will attach, but I am open to something new as well.
Things to include:
Name:
Title:
Phone:
Email:
Wanting something that is professional but attention grabbing.
Also we do a lot of work using drones on natural gas pipelines (leading the future)if you want to include any of that. I'm open to ideas.
Target Market(s)
Natural gas transmission industry / greenhouse gas mitigation industry
Industry/Entity Type
Business
Contact Information for Business Card
All details have been conveyed above.
Colors
Designer to choose colors to be used in the design.
Look and feel
Each slider illustrates characteristics of the customer's brand and the style your logo design should communicate.

```html
<!DOCTYPE html>
<html lang="en">
<head>
<meta charset="utf-8">
<title>KV Field Inspections – Business Card</title>
<link href="https://fonts.googleapis.com/css2?family=Roboto+Condensed:wght@400;500;700&display=swap" rel="stylesheet">
<style>
  :root {
    --stage: #ecebe8;
    --card-red: #c42128;
    --card-dark: #3a3a3c;
    --card-white: #ffffff;
    --ink-light: #ffffff;
    --ink-dark: #3a3a3c;
  }
  * { margin: 0; padding: 0; box-sizing: border-box; }
  html, body {
    width: 1200px; height: 1000px; overflow: hidden;
    background: var(--stage);
    font-family: "Roboto Condensed", Arial, sans-serif;
  }
  .stage { position: relative; width: 1200px; height: 1000px; }
  .card {
    position: absolute; width: 540px; height: 310px;
    box-shadow: 0 6px 18px rgba(0,0,0,0.18);
    overflow: hidden;
  }
  .card-front { left: 70px; top: 170px; background: var(--card-red); }
  .card-back { left: 590px; top: 520px; background: var(--card-white); }

  .front-side-panel {
    position: absolute; right: 0; top: 0; width: 180px; height: 100%;
    background: var(--card-dark);
  }
  .front-side-stripe {
    position: absolute; right: 180px; top: 0; width: 34px; height: 100%;
    background: var(--card-white);
  }
  .identity { position: absolute; left: 48px; top: 92px; color: var(--ink-light); }
  .identity-name { font-size: 30px; font-weight: 700; letter-spacing: 0.5px; line-height: 1; }
  .identity-title { font-size: 20px; font-weight: 400; margin-top: 4px; }

  .contact-list {
    position: absolute; left: 48px; top: 182px; list-style: none;
    color: var(--ink-light); font-size: 14px; line-height: 1.2;
  }
  .contact-item { display: flex; align-items: flex-start; gap: 12px; margin-bottom: 7px; }
  .contact-icon { width: 13px; height: 13px; flex: none; margin-top: 2px; fill: var(--ink-light); }

  .brand {
    position: absolute; left: 50%; top: 50%; transform: translate(-50%, -50%);
    display: flex; align-items: center; gap: 14px;
  }
  .brand-square { width: 46px; height: 46px; background: var(--card-red); }
  .brand-name { font-size: 34px; font-weight: 700; color: var(--ink-dark); white-space: nowrap; }
</style>
</head>
<body>
<main class="stage">
  <section class="card card-front" aria-label="Business card front">
    <div class="front-side-stripe"></div>
    <div class="front-side-panel"></div>
    <div class="identity">
      <div class="identity-name">JOHN DOE</div>
      <div class="identity-title">Manager</div>
    </div>
    <ul class="contact-list">
      <li class="contact-item">
        <svg class="contact-icon" viewBox="0 0 16 16"><path d="M3 1h3l1.5 4-2 1.3a9 9 0 0 0 4.2 4.2L11 8.5l4 1.5v3a2 2 0 0 1-2 2A12 12 0 0 1 1 3a2 2 0 0 1 2-2z"/></svg>
        <span>123 456 789</span>
      </li>
      <li class="contact-item">
        <svg class="contact-icon" viewBox="0 0 16 16"><path d="M8 0a8 8 0 1 0 0 16A8 8 0 0 0 8 0zm5.9 7h-2.5a12 12 0 0 0-1-4.6A6 6 0 0 1 13.9 7zM8 2c.8 1 1.3 2.8 1.4 5H6.6C6.7 4.8 7.2 3 8 2zM5.6 2.4A12 12 0 0 0 4.6 7H2.1a6 6 0 0 1 3.5-4.6zM2.1 9h2.5a12 12 0 0 0 1 4.6A6 6 0 0 1 2.1 9zM8 14c-.8-1-1.3-2.8-1.4-5h2.8c-.1 2.2-.6 4-1.4 5zm2.4-.4a12 12 0 0 0 1-4.6h2.5a6 6 0 0 1-3.5 4.6z"/></svg>
        <span>www.youesitegoeshere.com</span>
      </li>
      <li class="contact-item">
        <svg class="contact-icon" viewBox="0 0 16 16"><path d="M0 3h16v1.2L8 9 0 4.2z"/><path d="M0 5.6l8 4.8 8-4.8V13H0z"/></svg>
        <span>email@domaingoeshere.com</span>
      </li>
      <li class="contact-item">
        <svg class="contact-icon" viewBox="0 0 16 16"><path d="M8 0a5.5 5.5 0 0 0-5.5 5.5C2.5 10 8 16 8 16s5.5-6 5.5-10.5A5.5 5.5 0 0 0 8 0zm0 8a2.5 2.5 0 1 1 0-5 2.5 2.5 0 0 1 0 5z"/></svg>
        <span>Street Name, Zip Code<br>1234, City</span>
      </li>
    </ul>
  </section>

  <section class="card card-back" aria-label="Business card back">
    <div class="brand">
      <div class="brand-square"></div>
      <div class="brand-name">KV Field Inspections</div>
    </div>
  </section>
</main>
</body>
</html>
```